PrairieKite - New Website Design

Create a professional Shopify website for the hottest trend; a box of school supplies subscription box business called PrairieKite. Wexelo.com is an easy to use website builder.
Please see fernwhistle.com; lunapebble.com; quietmeadowfolk.com; and tovinjar.com for the concept I am after. The business has not been launched yet, I am currently in the pre-launch stage using a specialized landing page website, and so the time scale for developing my professional looking Shopify website is up to 1-2 weeks.
The webpage should have a fun feel and should match the style of the company logo at lunapebble.com. The pages to include are 'Home', 'About us' and 'Get Started'
Thank you and good luck!

```html
<!DOCTYPE html>
<html lang="en">
<head>
<meta charset="utf-8">
<title>PrairieKite – School Supplies Subscription Box</title>
<link rel="stylesheet" href="https://fonts.googleapis.com/css2?family=Fredoka:wght@600&family=Roboto+Condensed:wght@400;700&family=Yellowtail&display=swap">
<style>
  :root {
    --pink: #ff1166;
    --blue: #14a8e8;
    --teal: #2ed9c3;
    --ink: #141414;
    --body: #5c5c5c;
    --muted: #8a8a8a;
    --light: #f1f1f1;
    --footer: #2b2a2e;
    --footer-line: #3c3b40;
    --white: #ffffff;
  }
  * { box-sizing: border-box; margin: 0; padding: 0; }
  html, body { width: 1200px; height: 2233px; overflow: hidden; }
  body {
    position: relative;
    background: var(--white);
    font-family: "Roboto Condensed", Arial, sans-serif;
    color: var(--body);
  }
  a { text-decoration: none; color: inherit; }
  .btn {
    position: absolute;
    display: flex; align-items: center; justify-content: center;
    color: var(--white);
    font-weight: 700; font-size: 16px;
    border-radius: 2px;
  }
  .btn--pink { background: var(--pink); }
  .btn--blue { background: var(--blue); }
  .btn--teal { background: var(--teal); }
  .script-title {
    position: absolute; left: 0; right: 0;
    text-align: center;
    font-family: "Yellowtail", cursive;
    font-size: 40px; color: var(--ink); font-weight: 400;
  }

  /* Header */
  .site-header { position: absolute; top: 0; left: 0; width: 1200px; height: 68px; background: var(--white); }
  .brand {
    position: absolute; left: 112px; top: 16px;
    display: flex; align-items: center; gap: 10px;
    font-weight: 700; font-size: 28px; color: var(--teal);
  }
  .brand__dot { width: 26px; height: 26px; border-radius: 50%; background: var(--teal); }
  .main-nav a { position: absolute; top: 25px; font-size: 15px; color: var(--blue); }
  .main-nav .is-cta { color: var(--pink); }

  /* Hero */
  .hero {
    position: absolute; top: 68px; left: 0; width: 1200px; height: 514px;
    background: radial-gradient(ellipse at 40% 40%, #2e2e2e 0%, #161616 55%, #060606 100%);
    overflow: hidden;
  }
  .hero__floor { position: absolute; left: 0; bottom: 0; width: 100%; height: 30px; background: linear-gradient(#3a2a1c, #1e150d); }
  .hero__title {
    position: absolute; left: 112px; top: 112px;
    font-family: "Fredoka", sans-serif; font-weight: 600;
    font-size: 34px; line-height: 38px; letter-spacing: 1px;
    color: var(--white); text-transform: uppercase;
  }
  .hero__text { position: absolute; left: 112px; top: 200px; width: 420px; font-size: 15px; line-height: 22px; color: #e9e9e9; }
  .hero__art {
    position: absolute; left: 425px; top: 155px; width: 665px; height: 359px;
    background: radial-gradient(ellipse at 60% 60%, #c9a06b 0%, #b8844f 35%, rgba(80,60,40,0.4) 70%, rgba(0,0,0,0) 100%);
    border-radius: 12px;
  }

  /* How it works */
  .steps { position: absolute; top: 582px; left: 0; width: 1200px; height: 469px; }
  .step { position: absolute; top: 121px; width: 280px; text-align: center; }
  .step__badge {
    width: 68px; height: 68px; margin: 0 auto;
    display: flex; align-items: center; justify-content: center;
    border-radius: 50% 50% 50% 50% / 60% 60% 40% 40%;
    font-family: "Fredoka", sans-serif; font-style: italic;
    font-size: 24px; color: var(--white);
  }
  .step__title { margin-top: 26px; font-size: 18px; font-weight: 700; color: var(--ink); }
  .step__text { margin-top: 12px; font-size: 15px; line-height: 22px; color: var(--body); }

  /* Inside the box */
  .inside {
    position: absolute; top: 1051px; left: 0; width: 1200px; height: 441px;
    background: linear-gradient(120deg, #f7f7f7 0%, #e9e9e9 50%, #f4f4f4 100%);
  }
  .inside__art {
    position: absolute; left: 112px; top: 81px; width: 476px; height: 312px;
    background: radial-gradient(ellipse at 60% 55%, #e8b27a 0%, #d8a06a 30%, #8fb0d8 55%, rgba(233,233,233,0) 78%);
    border-radius: 12px;
  }
  .inside .script-title { left: 655px; right: auto; width: 390px; top: 82px; }
  .inside__text {
    position: absolute; left: 655px; top: 140px; width: 390px;
    text-align: center; font-size: 15px; line-height: 22.5px; color: var(--body);
  }

  /* Testimonials */
  .reviews { position: absolute; top: 1492px; left: 0; width: 1200px; height: 497px; }
  .reviews__divider { position: absolute; left: 599px; top: 128px; width: 1px; height: 241px; background: #e6e6e6; }
  .review { position: absolute; top: 130px; width: 440px; text-align: center; }
  .review__avatar {
    width: 104px; height: 104px; margin: 0 auto;
    border-radius: 50%; border: 3px solid var(--blue);
    background: linear-gradient(135deg, #d9b08a, #a97b55);
  }
  .review__quote { margin-top: 20px; font-size: 15px; line-height: 22px; color: var(--body); }
  .review__name { margin-top: 12px; font-size: 16px; font-weight: 700; color: var(--pink); }
  .review__role { font-size: 13px; color: var(--muted); }

  /* Footer */
  .site-footer { position: absolute; top: 1989px; left: 0; width: 1200px; height: 244px; background: var(--footer); color: #cfcfcf; }
  .footer-brand {
    position: absolute; left: 112px; top: 48px;
    display: flex; align-items: center; gap: 10px;
    font-weight: 700; font-size: 22px; color: var(--teal);
  }
  .footer-brand__dot { width: 20px; height: 20px; border-radius: 50%; background: var(--teal); }
  .footer-col { position: absolute; top: 36px; }
  .footer-col h4 { font-size: 14px; font-weight: 700; color: var(--white); margin-bottom: 10px; }
  .footer-col li { list-style: none; font-size: 13px; line-height: 22px; }
  .social { display: flex; gap: 3px; }
  .social span { width: 27px; height: 27px; border-radius: 50%; border: 1.5px solid #bdbdbd; }
  .newsletter { position: absolute; left: 864px; top: 28px; width: 224px; }
  .newsletter h4 { font-family: "Yellowtail", cursive; font-weight: 400; font-size: 21px; color: var(--white); margin-bottom: 14px; }
  .newsletter__input { height: 36px; background: var(--white); border-radius: 2px; padding-left: 12px; display: flex; align-items: center; font-size: 14px; color: #9a9a9a; }
  .newsletter__btn { position: static; margin-top: 9px; height: 36px; }
  .footer-bar { position: absolute; left: 112px; top: 195px; width: 978px; border-top: 1px solid var(--footer-line); }
  .footer-copy { position: absolute; left: 112px; top: 213px; font-size: 13px; }
  .footer-legal { position: absolute; right: 110px; top: 213px; font-size: 13px; display: flex; gap: 12px; }
</style>
</head>
<body>

<header class="site-header">
  <a class="brand" href="#"><span class="brand__dot"></span>PrairieKite</a>
  <nav class="main-nav">
    <a href="#" style="left:862px">Home</a>
    <a href="#" style="left:932px">About Us</a>
    <a href="#" class="is-cta" style="left:1021px">Get Started</a>
  </nav>
</header>

<section class="hero">
  <div class="hero__floor"></div>
  <div class="hero__art" role="img" aria-label="Cardboard box overflowing with school supplies, pencil cup, globe and toy school bus"></div>
  <h1 class="hero__title">Lorem ipsum dolor sit amet<br>as well as consectetur</h1>
  <p class="hero__text">Nullam ac urna eu felis dapibus condimentum sit amet a augue. Sed non neque elit. Sed ut imperdiet nisi. Proin condimentum fermentum nunc.</p>
  <a class="btn btn--pink" href="#" style="left:112px; top:289px; width:141px; height:39px;">Get Started</a>
  <a class="btn btn--blue" href="#" style="left:262px; top:289px; width:140px; height:39px;">Give A Gift</a>
</section>

<section class="steps">
  <h2 class="script-title" style="top:40px">How it Works</h2>
  <div class="step" style="left:125px">
    <div class="step__badge" style="background:var(--blue)">01</div>
    <h3 class="step__title">Lorem ipsum dolor sit</h3>
    <p class="step__text">Duis sed odio sit amet nibh vulputate cursus a sit amet mauris. Morbi accumsan ipsum Nam nec tellus a odio tincidunt auctor a ornare odio. neque elit.</p>
  </div>
  <div class="step" style="left:459px">
    <div class="step__badge" style="background:var(--pink)">02</div>
    <h3 class="step__title">Lorem ipsum dolor sit</h3>
    <p class="step__text">Duis sed odio sit amet nibh vulputate cursus a sit amet mauris. Morbi accumsan ipsum Nam nec tellus a odio tincidunt auctor a ornare odio. neque elit.</p>
  </div>
  <div class="step" style="left:794px">
    <div class="step__badge" style="background:var(--teal)">03</div>
    <h3 class="step__title">Lorem ipsum dolor sit</h3>
    <p class="step__text">Duis sed odio sit amet nibh vulputate cursus a sit amet mauris. Morbi accumsan ipsum Nam nec tellus a odio tincidunt auctor a ornare odio. neque elit.</p>
  </div>
  <a class="btn btn--pink" href="#" style="left:530px; top:378px; width:140px; height:39px;">Get Started</a>
</section>

<section class="inside">
  <div class="inside__art" role="img" aria-label="Open cardboard box with notebooks, colored pencils and pens beside it"></div>
  <h2 class="script-title">What’s inside the Box</h2>
  <p class="inside__text">Class aptent taciti sociosqu ad litora torquent per conubia nostra, per inceptos himenaeos. Mauris in erat justo. Nullam ac urna eu felis dapibus condimentum sit amet a augue. Sed non neque elit. Sed ut imperdiet nisi. Proin condimentum fermentum nunc. Etiam pharetra, erat sed fermentum feugiat, velit mauris egestas quam, ut aliquam massa nisl quis neque. Suspendisse in orci enim.</p>
  <a class="btn btn--teal" href="#" style="left:780px; top:316px; width:140px; height:39px;">Explore More</a>
</section>

<section class="reviews">
  <h2 class="script-title" style="top:44px">Happy Customer</h2>
  <div class="reviews__divider"></div>
  <div class="review" style="left:128px">
    <div class="review__avatar" role="img" aria-label="Portrait photo of customer Sophia"></div>
    <p class="review__quote">“ Proin condimentum fermentum nunc. Etiam pharetra, erat sed fermentum feugiat, velit mauris egestas quam, ut aliquam massa nisl quis neque. Suspendisse in orci velit mauris egestas quam enim.”</p>
    <p class="review__name">Sophia</p>
    <p class="review__role">lorem ipsum dolor</p>
  </div>
  <div class="review" style="left:633px">
    <div class="review__avatar" role="img" aria-label="Portrait photo of customer William doe"></div>
    <p class="review__quote">“ Proin condimentum fermentum nunc. Etiam pharetra, erat sed fermentum feugiat, velit mauris egestas quam, ut aliquam massa nisl quis neque. Suspendisse in orci velit mauris egestas quam enim.”</p>
    <p class="review__name">William doe</p>
    <p class="review__role">lorem ipsum dolor</p>
  </div>
  <a class="btn btn--blue" href="#" style="left:475px; top:408px; width:252px; height:39px;">View More Customer Reviews</a>
</section>

<footer class="site-footer">
  <a class="footer-brand" href="#"><span class="footer-brand__dot"></span>PrairieKite</a>
  <div class="footer-col" style="left:317px">
    <h4>Subscribe</h4>
    <ul><li>Get Started</li><li>Get a PrairieKite</li><li>Give a Gift</li><li>Claim a Gift</li></ul>
  </div>
  <div class="footer-col" style="left:505px">
    <h4>Info</h4>
    <ul><li>About PrairieKite</li><li>Our Story</li><li>Contact Us</li><li>FAQs</li></ul>
  </div>
  <div class="footer-col" style="left:660px">
    <h4>We’re Social</h4>
    <div class="social"><span></span><span></span><span></span><span></span><span></span></div>
  </div>
  <div class="newsletter">
    <h4>Subcribe Newsletter</h4>
    <div class="newsletter__input">Name</div>
    <a class="btn btn--teal newsletter__btn" href="#">Subscribe</a>
  </div>
  <div class="footer-bar"></div>
  <p class="footer-copy">Copyright ©2017 PrairieKite.</p>
  <p class="footer-legal"><span>Terms of Use</span><span>Privacy</span><span>Sitemap</span></p>
</footer>

</body>
</html>
```